Letterhead for New Orthopaedic Surgery Practice

My husband and I are starting our own practice named RB Spine & Vitality Center. We would like to create a nice simple but high class letterhead that doesn't use too much solid color ink when printing. I like the colors dark blue, gold, yellow. Open to other suggestions. We will need to list him and I both on the top of the letterhead. Here is the important information:
Lucinda Perrow, M.D. - Hand and Upper Extremity Surgery
Abena Quist, M.D. - Hip & Knee Replacement/General Orthopaedic Surgery
Location: 18735 North Harlow Pkwy
Maple Heights, OH 44137
Phone: 216-218-4650
Fax: 216-582-1346
Email: info@myrbspine.com

The only thing is that the phone and fax numbers will change once we get into our space. I just want to get the design started. I am including several documents which are my previous practice letterhead, my current procedure room letterhead, and our new Logo. The other letterheads are just for examples but please think outside of the box! We would love to see some great designs.

Colors
0054AA
0677BA
7BADD7
CADEEF
E8F1F8
0094D4
00A9DD
6FCCEA
C7EBF8
E9F6FB

Requirements
Must have
• class, elegance, luxury

```html
<!DOCTYPE html>
<html lang="en">
<head>
<meta charset="utf-8">
<title>RB Spine &amp; Vitality Center – Letterhead</title>
<link rel="stylesheet" href="https://fonts.googleapis.com/css2?family=Arimo:wght@400;700&display=swap">
<style>
  :root {
    --navy: #14254a;
    --gold: #c9a45c;
    --paper: #ffffff;
  }
  * { margin: 0; padding: 0; box-sizing: border-box; }
  html, body {
    width: 927px;
    height: 1200px;
    overflow: hidden;
    background: var(--paper);
  }
  .letterhead {
    position: relative;
    width: 927px;
    height: 1200px;
    font-family: "Arimo", Arial, sans-serif;
    color: var(--navy);
  }
  .brand {
    position: absolute;
    left: 140px;
    top: 73px;
    width: 124px;
    height: 124px;
    display: flex;
    align-items: center;
    justify-content: center;
    flex-direction: column;
    gap: 6px;
  }
  .brand-circle {
    width: 14px;
    height: 14px;
    border-radius: 50%;
    background: var(--gold);
  }
  .brand-name {
    font-size: 14px;
    font-weight: 700;
    line-height: 1.25;
    text-align: center;
    color: var(--navy);
    letter-spacing: 0.3px;
  }
  .physicians {
    position: absolute;
    left: 294px;
    top: 102px;
    width: 600px;
    font-size: 17.2px;
    line-height: 21.5px;
  }
  .physician + .physician { margin-top: 5px; }
  .physician-name { font-weight: 700; }
  .physician-line { display: block; white-space: nowrap; }
  .rule {
    position: absolute;
    left: 133px;
    width: 681px;
    height: 2px;
    background: var(--gold);
  }
  .rule-top { top: 231px; }
  .rule-bottom { top: 1081px; }
  .contact {
    position: absolute;
    left: 0;
    top: 1103px;
    width: 927px;
    text-align: center;
    font-size: 14px;
    line-height: 17px;
  }
  .contact-sep { margin: 0 10px; }
</style>
</head>
<body>
  <div class="letterhead">
    <div class="brand">
      <span class="brand-circle"></span>
      <span class="brand-name">RB Spine &amp;<br>Vitality Center</span>
    </div>

    <div class="physicians">
      <p class="physician"><span class="physician-line"><span class="physician-name">Lucinda Perrow, M.D.</span> - Hand and Upper Extremity Surgery</span></p>
      <p class="physician"><span class="physician-line"><span class="physician-name">Abena Quist, M.D.</span> - Hip &amp; Knee Replacement / General Orthopaedic</span><span class="physician-line">Surgery</span></p>
    </div>

    <div class="rule rule-top"></div>
    <div class="rule rule-bottom"></div>

    <div class="contact">
      <p class="contact-address">18735 North Harlow Pkwy, Maple Heights, OH 44137</p>
      <p class="contact-lines">Phone: 216-218-4650<span class="contact-sep">|</span>Fax: 216-582-1346<span class="contact-sep">|</span>Email: info@myrbspine.com</p>
    </div>
  </div>
</body>
</html>
```